Website design for management consulting firm

We need a web design for a new consulting company based in Boston, MA called "Fernhollow Ridge Consulting." This webpage will be simple home page, with a "contact us" page, that describes the services of the consulting firm. The company provides strategic planning, business assessment, process re-designs, and other management consulting functions. I would like the website to look high-tech. A logo was already created via Pixel Harbor.

Target Market(s)

Other business owners across a wide spectrum of industries - from IT to retail.

Industry/Entity Type

It Company

Number of Pages Required

3 page

Colors
0455a3
ffffff

Requirements
Must have
• Front page that provides generic text / overview of the firm. A "services" tab that describes consulting services. A "contact us" tab that provides either a form to contact us or just the contact email address of the company. info@fernhollowridgeconsulting.example

```html
<!DOCTYPE html>
<html lang="en">
<head>
<meta charset="utf-8">
<title>Fernhollow Ridge Consulting</title>
<link rel="stylesheet" href="https://fonts.googleapis.com/css2?family=Arimo:wght@400;700&display=swap">
<style>
  :root {
    --brand: #0455a3;
    --white: #ffffff;
    --ink: #1c1c1c;
    --muted: #777777;
    --line: #c9c9c9;
    --card-line: #d4d4d4;
  }
  * { box-sizing: border-box; margin: 0; padding: 0; }
  html, body { width: 1200px; height: 3386px; overflow: hidden; }
  body { font-family: "Arimo", Arial, sans-serif; color: var(--ink); background: var(--white); position: relative; }

  .page-section { position: absolute; left: 0; width: 1200px; }

  /* Header */
  .site-header { height: 125px; background: var(--white); }
  .brand { position: absolute; left: 47px; top: 40px; display: flex; align-items: center; gap: 12px; }
  .brand-square { width: 44px; height: 44px; background: var(--brand); }
  .brand-name { font-size: 30px; font-weight: 700; color: var(--ink); letter-spacing: -0.5px; }
  .main-nav { position: absolute; top: 57px; left: 0; width: 1200px; }
  .main-nav a { position: absolute; font-size: 17px; font-weight: 700; letter-spacing: 1.5px; color: var(--muted); text-decoration: none; }
  .main-nav a.is-active { color: var(--brand); }
  .nav-home { left: 748px; }
  .nav-services { left: 864px; }
  .nav-contact { left: 1007px; }

  /* Banners */
  .banner { position: absolute; left: 0; width: 1200px; overflow: hidden; }
  .banner-photo { position: absolute; inset: 0; }
  .hero { top: 125px; height: 480px; }
  .hero .banner-photo { background: linear-gradient(90deg, #a9bfdc 0%, #d4deeb 30%, #eef1f6 45%, #3b4d6b 62%, #1e2c47 80%, #c9d2de 100%); }
  .hero-kicker { position: absolute; left: 48px; top: 232px; font-size: 21px; font-weight: 700; color: var(--white); letter-spacing: 1px; }
  .hero-title { position: absolute; left: 46px; top: 256px; font-size: 78px; line-height: 72px; font-weight: 700; color: var(--white); letter-spacing: 2px; }
  .slider-dots { position: absolute; right: 22px; bottom: 24px; display: flex; gap: 12px; }
  .slider-dots span { width: 11px; height: 11px; border-radius: 50%; background: rgba(255,255,255,0.6); }
  .slider-dots span.is-current { background: var(--white); }

  .page-banner { height: 245px; }
  .page-banner-title { position: absolute; left: 50px; top: 150px; font-size: 52px; font-weight: 700; color: rgba(255,255,255,0.75); letter-spacing: 2px; }
  .services-banner { top: 1217px; }
  .services-banner .banner-photo { background: linear-gradient(100deg, #8d949c 0%, #c9ced3 35%, #e6e8ea 55%, #f4f4f4 75%, #d9dcdf 100%); }
  .contact-banner { top: 2490px; }
  .contact-banner .banner-photo { background: linear-gradient(100deg, #e8e4dc 0%, #d9d9d9 40%, #9a9da2 60%, #b89a80 80%, #e2cbb4 100%); }

  /* Features */
  .features { top: 605px; height: 381px; }
  .feature { position: absolute; top: 50px; width: 276px; }
  .feature-1 { left: 72px; }
  .feature-2 { left: 447px; }
  .feature-3 { left: 821px; }
  .feature-icon { display: block; margin: 0 auto; height: 80px; }
  .feature-title { margin: 22px -40px 0; text-align: center; white-space: nowrap; font-size: 19px; font-weight: 700; letter-spacing: 1.2px; }
  .feature-text { margin-top: 22px; font-size: 12.5px; line-height: 16.2px; text-align: justify; hyphens: auto; }

  /* Footer */
  .site-footer { height: 104px; background: var(--brand); color: var(--white); }
  .footer-brand { position: absolute; left: 70px; top: 38px; display: flex; align-items: center; gap: 9px; }
  .footer-brand .brand-square { width: 26px; height: 26px; background: var(--white); }
  .footer-brand .brand-name { font-size: 18px; color: var(--white); }
  .copyright { position: absolute; left: 492px; top: 45px; font-size: 14px; }
  .footer-nav a { position: absolute; top: 45px; font-size: 14px; color: var(--white); text-decoration: none; }
  .footer-nav .f-home { left: 885px; }
  .footer-nav .f-services { left: 972px; }
  .footer-nav .f-contact { left: 1057px; }

  /* Services */
  .services-intro { position: absolute; left: 70px; top: 1494px; width: 1060px; font-size: 13px; line-height: 17.6px; text-align: justify; hyphens: auto; }
  .services-intro strong { font-style: italic; }
  .service-card { position: absolute; width: 302px; height: 222px; border: 2px solid var(--card-line); border-radius: 12px; padding: 28px 0 0 26px; }
  .service-card h3 { font-size: 17px; font-weight: 700; color: var(--brand); letter-spacing: 1px; }
  .service-card ul { margin-top: 20px; list-style: none; }
  .service-card li { font-size: 13px; line-height: 16px; }
  .service-card li::before { content: "•"; display: inline-block; width: 14px; }
  .col-1 { left: 70px; } .col-2 { left: 445px; } .col-3 { left: 816px; }
  .row-1 { top: 1640px; } .row-2 { top: 1908px; }

  /* Contact */
  .contact-info { position: absolute; left: 70px; top: 2772px; }
  .info-block { position: relative; padding-left: 38px; margin-bottom: 28px; }
  .info-block svg { position: absolute; left: 0; top: 0; }
  .info-label { font-size: 14px; font-weight: 700; color: var(--brand); letter-spacing: 1px; }
  .info-value { margin-top: 14px; margin-left: 3px; font-size: 13.5px; }
  .contact-form { position: absolute; left: 492px; top: 2770px; width: 640px; }
  .form-intro { font-size: 13.5px; line-height: 17.6px; }
  .field { margin-top: 20px; width: 416px; }
  .field label { display: block; font-size: 13px; font-weight: 700; color: var(--brand); letter-spacing: 1px; margin-bottom: 8px; }
  .field input, .field textarea { display: block; width: 416px; height: 20px; border: 1px solid var(--line); background: var(--white); font: inherit; }
  .field textarea { height: 88px; resize: none; }
  .form-note { width: 416px; margin-top: 18px; text-align: right; font-size: 13px; font-style: italic; color: #444; }
  .send-button { display: block; margin-top: 16px; width: 110px; height: 22px; border: 0; background: var(--brand); color: var(--white); font: 700 13px "Arimo", Arial, sans-serif; letter-spacing: 1px; }
</style>
</head>
<body>

<!-- Home -->
<header class="page-section site-header" style="top:0">
  <div class="brand"><span class="brand-square"></span><span class="brand-name">Fernhollow Ridge</span></div>
  <nav class="main-nav"><a class="nav-home is-active" href="#">HOME</a><a class="nav-services" href="#">SERVICES</a><a class="nav-contact" href="#">CONTACT US</a></nav>
</header>

<section class="banner hero">
  <div class="banner-photo" role="img" aria-label="Photo of three business people in suits reviewing documents at a glass office table"></div>
  <p class="hero-kicker">WELCOME TO FERNHOLLOW RIDGE</p>
  <h1 class="hero-title">HELP US<br>HELP YOU!</h1>
  <div class="slider-dots"><span></span><span></span><span class="is-current"></span></div>
</section>

<section class="page-section features">
  <div class="feature feature-1">
    <svg class="feature-icon" width="110" height="80" viewBox="0 0 110 80" aria-hidden="true">
      <path d="M2 28 L22 18 L34 48 L14 58 Z" fill="var(--brand)"/>
      <path d="M108 28 L88 18 L76 48 L96 58 Z" fill="var(--brand)"/>
      <path d="M26 24 L50 20 L62 28 L84 22 L78 46 L60 62 L40 54 L30 46 Z" fill="var(--brand)"/>
      <path d="M48 30 L60 38" stroke="var(--white)" stroke-width="3"/>
    </svg>
    <h2 class="feature-title">YOUR PERFECT PARTNER</h2>
    <p class="feature-text">Lorem ipsum dolor sit amet, consectetur adipiscing elit. Praesent eget lectus nec lorem eleifend pellentesque. Ut pulvinar elementum odio. Donec nec augue a dui bibendum placerat tempus sed ipsum. Ut orci augue, venenatis vel pulvinar id, dapibus in nisl. Suspendisse consequat eget</p>
  </div>
  <div class="feature feature-2">
    <svg class="feature-icon" width="60" height="80" viewBox="0 0 60 80" aria-hidden="true">
      <rect x="10" y="8" width="40" height="38" rx="8" fill="var(--brand)"/>
      <rect x="16" y="44" width="28" height="34" fill="var(--brand)"/>
      <path d="M20 10 V30 M30 10 V30 M40 10 V30" stroke="var(--white)" stroke-width="2.5"/>
    </svg>
    <h2 class="feature-title">STRONG ALLIANCE</h2>
    <p class="feature-text">Lorem ipsum dolor sit amet, consectetur adipiscing elit. Praesent eget lectus nec lorem eleifend pellentesque. Ut pulvinar elementum odio. Donec nec augue a dui bibendum placerat tempus sed ipsum. Ut orci augue, venenatis vel pulvinar id, dapibus in nisl. Suspendisse consequat eget</p>
  </div>
  <div class="feature feature-3">
    <svg class="feature-icon" width="80" height="80" viewBox="0 0 80 80" aria-hidden="true">
      <rect x="6" y="36" width="16" height="38" fill="var(--brand)"/>
      <path d="M26 36 L40 10 Q48 6 48 16 L44 32 H68 Q76 34 72 42 L66 70 Q64 74 58 74 H26 Z" fill="var(--brand)"/>
    </svg>
    <h2 class="feature-title">TRUSTED WORKFORCE</h2>
    <p class="feature-text">Lorem ipsum dolor sit amet, consectetur adipiscing elit. Praesent eget lectus nec lorem eleifend pellentesque. Ut pulvinar elementum odio. Donec nec augue a dui bibendum placerat tempus sed ipsum. Ut orci augue, venenatis vel pulvinar id, dapibus in nisl. Suspendisse consequat eget</p>
  </div>
</section>

<footer class="page-section site-footer" style="top:986px">
  <div class="footer-brand"><span class="brand-square"></span><span class="brand-name">Fernhollow Ridge</span></div>
  <p class="copyright">Fernhollow Ridge Consulting © 2015</p>
  <nav class="footer-nav"><a class="f-home" href="#">Home</a><a class="f-services" href="#">Services</a><a class="f-contact" href="#">Contact Us</a></nav>
</footer>

<!-- Services -->
<header class="page-section site-header" style="top:1090px">
  <div class="brand"><span class="brand-square"></span><span class="brand-name">Fernhollow Ridge</span></div>
  <nav class="main-nav"><a class="nav-home" href="#">HOME</a><a class="nav-services is-active" href="#">SERVICES</a><a class="nav-contact" href="#">CONTACT US</a></nav>
</header>

<section class="banner page-banner services-banner">
  <div class="banner-photo" role="img" aria-label="Photo of a businessman's hands with a wristwatch resting on a desk beside a glass"></div>
  <h1 class="page-banner-title">SERVICES</h1>
</section>

<p class="services-intro"><strong>Fernhollow Ridge Consulting</strong> consectetur adipiscing elit. Praesent eget lectus nec lorem eleifend pellentesque. Ut pulvinar elementum odio. Donec nec augue a dui bibendum placerat tempus sed ipsum. Ut orci augue, venenatis vel pulvinar id, dapibus in nisl. Suspendisse consequat eget felis et sollicitudin. Nulla vel erat quis est vehicula tincidunt. Etiam eu nibh tincidunt, gravida dolor ac, malesuada risus. Aenean finibus sem nec metus luctus, sit amet tempor nunc consectetur. Pellentesque aliquam sapien dui, id faucibus tellus posuere et. Duis libero diam, mollis eu dui sed, finibus mollis ex. Praesent congue, neque sit amet lobortis scelerisque, nisl justo suscipit erat, id egestas dui massa nec augue. Sed sed sollicitudin velit. Donec et erat at odio condimentum vestibulum. Nulla ante odio, luctus vel risus ut, vestibulum molestie arcu.</p>

<article class="service-card col-1 row-1"><h3>AUDIT &amp; ASSURANCE</h3><ul><li>Accounting advisory services</li><li>Board governance advisory</li><li>Financial statement audit</li><li>IFRS readiness and conversions</li><li>Regulatory compliance and reporting</li><li>Sustainable business solutions</li><li>Valuation services</li></ul></article>
<article class="service-card col-2 row-1"><h3>AUDIT &amp; ASSURANCE</h3><ul><li>Accounting advisory services</li><li>Board governance advisory</li><li>Financial statement audit</li><li>IFRS readiness and conversions</li><li>Regulatory compliance and reporting</li><li>Sustainable business solutions</li><li>Valuation services</li></ul></article>
<article class="service-card col-3 row-1"><h3>AUDIT &amp; ASSURANCE</h3><ul><li>Accounting advisory services</li><li>Board governance advisory</li><li>Financial statement audit</li><li>IFRS readiness and conversions</li><li>Regulatory compliance and reporting</li><li>Sustainable business solutions</li><li>Valuation services</li></ul></article>
<article class="service-card col-1 row-2"><h3>AUDIT &amp; ASSURANCE</h3><ul><li>Accounting advisory services</li><li>Board governance advisory</li><li>Financial statement audit</li><li>IFRS readiness and conversions</li><li>Regulatory compliance and reporting</li><li>Sustainable business solutions</li><li>Valuation services</li></ul></article>
<article class="service-card col-2 row-2"><h3>AUDIT &amp; ASSURANCE</h3><ul><li>Accounting advisory services</li><li>Board governance advisory</li><li>Financial statement audit</li><li>IFRS readiness and conversions</li><li>Regulatory compliance and reporting</li><li>Sustainable business solutions</li><li>Valuation services</li></ul></article>
<article class="service-card col-3 row-2"><h3>AUDIT &amp; ASSURANCE</h3><ul><li>Accounting advisory services</li><li>Board governance advisory</li><li>Financial statement audit</li><li>IFRS readiness and conversions</li><li>Regulatory compliance and reporting</li><li>Sustainable business solutions</li><li>Valuation services</li></ul></article>

<footer class="page-section site-footer" style="top:2247px; height:118px">
  <div class="footer-brand" style="top:44px"><span class="brand-square"></span><span class="brand-name">Fernhollow Ridge</span></div>
  <p class="copyright" style="top:51px">Fernhollow Ridge Consulting © 2015</p>
  <nav class="footer-nav"><a class="f-home" href="#" style="top:51px">Home</a><a class="f-services" href="#" style="top:51px">Services</a><a class="f-contact" href="#" style="top:51px">Contact Us</a></nav>
</footer>

<!-- Contact -->
<header class="page-section site-header" style="top:2365px">
  <div class="brand"><span class="brand-square"></span><span class="brand-name">Fernhollow Ridge</span></div>
  <nav class="main-nav"><a class="nav-home" href="#">HOME</a><a class="nav-services" href="#">SERVICES</a><a class="nav-contact is-active" href="#">CONTACT US</a></nav>
</header>

<section class="banner page-banner contact-banner">
  <div class="banner-photo" role="img" aria-label="Photo of a hand holding a smartphone above a laptop keyboard and printed charts"></div>
  <h1 class="page-banner-title">CONTACT US</h1>
</section>

<div class="contact-info">
  <div class="info-block">
    <svg width="22" height="22" viewBox="0 0 24 24" aria-hidden="true"><path d="M6.6 10.8a15.1 15.1 0 0 0 6.6 6.6l2.2-2.2a1 1 0 0 1 1-.25 11.4 11.4 0 0 0 3.6.57 1 1 0 0 1 1 1V20a1 1 0 0 1-1 1A17 17 0 0 1 3 4a1 1 0 0 1 1-1h3.5a1 1 0 0 1 1 1c0 1.25.2 2.45.57 3.57a1 1 0 0 1-.25 1z" fill="var(--brand)"/></svg>
    <p class="info-label">TELEPHONE NUMBER</p>
    <p class="info-value">1234 567 890</p>
  </div>
  <div class="info-block">
    <svg width="22" height="18" viewBox="0 0 22 16" aria-hidden="true"><rect x="0" y="0" width="22" height="16" fill="var(--brand)"/><path d="M1 1 L11 9 L21 1" stroke="var(--white)" stroke-width="1.8" fill="none"/></svg>
    <p class="info-label">EMAIL ADDRESS</p>
    <p class="info-value">info@fernhollowridgeconsulting.example</p>
  </div>
</div>

<form class="contact-form">
  <p class="form-intro">We're happy to hear anything from you. Just send us message using the form below. we'll keep in touch with you as soon as possible.</p>
  <div class="field"><label for="f-name">NAME *</label><input id="f-name" type="text"></div>
  <div class="field"><label for="f-email">EMAIL *</label><input id="f-email" type="email"></div>
  <div class="field"><label for="f-subject">SUBJECT *</label><input id="f-subject" type="text"></div>
  <div class="field"><label for="f-message">MESSAGE*</label><textarea id="f-message"></textarea></div>
  <p class="form-note">(fields with * are required)</p>
  <button class="send-button" type="button">SEND</button>
</form>

<footer class="page-section site-footer" style="top:3266px; height:120px">
  <div class="footer-brand" style="top:46px"><span class="brand-square"></span><span class="brand-name">Fernhollow Ridge</span></div>
  <p class="copyright" style="top:53px">Fernhollow Ridge Consulting © 2015</p>
  <nav class="footer-nav"><a class="f-home" href="#" style="top:53px">Home</a><a class="f-services" href="#" style="top:53px">Services</a><a class="f-contact" href="#" style="top:53px">Contact Us</a></nav>
</footer>

</body>
</html>
```